Business Card - Professional Minimalist - Double sided

We appreciate minimalist logo/web/collateral designs that allow design to tell a story. We want to relay a professional image/approach but throwing in a splash of modern when we’re able so long as it’s not distracting. Think 75% classic corporate, 25% modern. Open to black or white design, not sure which might look the best.

Target Market(s)

Senior executives or related government affairs contacts within the agriculture, energy, and defense industries (i.e., potential clients) but located outside of Washington, DC. Most potential clients based in DC with be familiar with both of us and our shared history.

Industry/Entity Type

Consulting

Contact Information for Business Card

Name: Derek M. Holloway
Title: Co-Founder & Partner
Address: 418 Linwood Terrace NE | Suite 2260 | Washington, D.C. 20017
Phone: (202) 555-0148
Email: Derek@BrimleyHolloway.example

Font styles to use
Serif

Colors

Designer to choose only greyscale colors for use in the design.

Requirements
Must have
• Name: Derek M. Holloway
Phone: (202) 555-0148

```html
<!DOCTYPE html>
<html lang="en">
<head>
<meta charset="utf-8">
<title>Brimley Holloway Group — Business Card</title>
<link href="https://fonts.googleapis.com/css2?family=Open+Sans:wght@400;600&family=Raleway:wght@700&display=swap" rel="stylesheet">
<style>
  :root {
    --backdrop: #000000;
    --card: #38383b;
    --ink: #ffffff;
    --ink-soft: #e4e4e6;
    --rule: #5a5a5e;
    --mark-muted: #8c8c90;
  }
  * { margin: 0; padding: 0; box-sizing: border-box; }
  html, body {
    width: 1200px; height: 900px; overflow: hidden;
    background: var(--backdrop);
  }
  .stage { position: relative; width: 1200px; height: 900px; }
  .card {
    position: absolute;
    width: 458px; height: 282px;
    border-radius: 13px;
    background: var(--card);
    overflow: hidden;
  }
  .card--front { left: 138px; top: 265px; }
  .card--back { left: 625px; top: 268px; }

  .brand {
    position: absolute;
    display: flex; align-items: center; gap: 10px;
    font-family: "Open Sans", sans-serif;
    font-weight: 600;
    text-transform: uppercase;
    white-space: nowrap;
  }
  .brand__square { flex: none; border: 2px solid currentColor; }
  .brand__name { line-height: 1.15; }
  .brand__sub { display: block; text-align: right; letter-spacing: 0.35em; }

  .brand--small { left: 24px; top: 122px; color: var(--ink); font-size: 13px; }
  .brand--small .brand__square { width: 30px; height: 30px; }
  .brand--small .brand__sub { font-size: 8px; }

  .brand--large { left: 77px; top: 106px; color: var(--mark-muted); font-size: 22px; }
  .brand--large .brand__square { width: 46px; height: 46px; }
  .brand--large .brand__sub { font-size: 12px; letter-spacing: 0.45em; }

  .divider {
    position: absolute; left: 226px; top: 71px;
    width: 1px; height: 138px; background: var(--rule);
  }
  .details {
    position: absolute; left: 238px; top: 70px; right: 12px;
    color: var(--ink-soft);
    font-family: "Open Sans", sans-serif;
    white-space: nowrap;
  }
  .details__name {
    font-family: "Raleway", sans-serif; font-weight: 700;
    font-size: 18px; color: var(--ink); text-transform: uppercase;
    line-height: 1.2;
  }
  .details__title { font-size: 11.5px; text-transform: uppercase; margin-top: 1px; }
  .contact { list-style: none; margin-top: 12px; font-size: 11.5px; }
  .contact__item { display: flex; align-items: center; gap: 5px; height: 17.5px; }
  .contact__icon { width: 13px; height: 13px; flex: none; }
  .details__address { margin-top: 10px; font-size: 11.5px; line-height: 16.5px; }
</style>
</head>
<body>
<main class="stage">
  <section class="card card--front" aria-label="Card front">
    <div class="brand brand--small">
      <span class="brand__square"></span>
      <span class="brand__name">Brimley Holloway<span class="brand__sub">Group</span></span>
    </div>
    <div class="divider"></div>
    <div class="details">
      <h1 class="details__name">Derek M. Holloway</h1>
      <p class="details__title">Co-Founder &amp; Partner</p>
      <ul class="contact">
        <li class="contact__item">
          <svg class="contact__icon" viewBox="0 0 16 16" fill="none" stroke="currentColor" stroke-width="1.4"><path d="M4 1.5l2.2 3-1.4 1.6c.8 1.9 2.3 3.4 4.2 4.2l1.6-1.4 3 2.2-1.4 2.4C7 13.3 2.7 9 2 3.1z"/></svg>
          (202) 555-0148
        </li>
        <li class="contact__item">
          <svg class="contact__icon" viewBox="0 0 16 16" fill="none" stroke="currentColor" stroke-width="1.4"><rect x="1" y="3" width="14" height="10"/><path d="M1 3l7 6 7-6"/></svg>
          Derek@BrimleyHolloway.example
        </li>
        <li class="contact__item">
          <svg class="contact__icon" viewBox="0 0 16 16" fill="none" stroke="currentColor" stroke-width="1.2"><circle cx="8" cy="8" r="6.5"/><ellipse cx="8" cy="8" rx="3" ry="6.5"/><path d="M1.5 8h13M2.5 4.8h11M2.5 11.2h11"/></svg>
          www.BrimleyHolloway.example
        </li>
      </ul>
      <p class="details__address">418 Linwood Terrace NE | Suite<br>2260 | Washington, D.C. 20017</p>
    </div>
  </section>

  <section class="card card--back" aria-label="Card back">
    <div class="brand brand--large">
      <span class="brand__square"></span>
      <span class="brand__name">Brimley Holloway<span class="brand__sub">Group</span></span>
    </div>
  </section>
</main>
</body>
</html>
```